Business Card Design

We need a business card design for a new company (Sole Proprietorship) based in Maryland,USA. We sell African wears & fabrics, headgears, trendy clothes, shoes and accessories.
We cater for men's and women's needs and we sell retail.
We would like to see designs that use a beautiful arrays of colors- The final design design should communicate FASHION.
Industry/Entity Type
Business
Contact Information for Business Card
Name: Folasade Okonkwo
Name of Business: Heritage & Style
Address: 27846 Birchmont Court, Fernhill, NV 20894
Telephone: 318-731-5096
E-mail: heritageandstyle@mailvora.net
Look and feel
Each slider illustrates characteristics of the customer's brand and the style your logo design should communicate.

```html
<!DOCTYPE html>
<html lang="en">
<head>
<meta charset="utf-8">
<title>Heritage &amp; Style — Business Card</title>
<link rel="stylesheet" href="https://fonts.googleapis.com/css2?family=Jost:wght@700&family=Arimo:wght@400&display=swap">
<style>
  :root {
    --backdrop: #d9d9d9;
    --card-black: #2b2b2e;
    --edge-teal: #1f9f86;
    --brand-red: #f2443f;
    --accent-yellow: #f7d31a;
    --text-white: #ffffff;
    --fabric-red: #d8322f;
    --fabric-blue: #2c3f9a;
    --fabric-yellow: #f2b51c;
    --fabric-teal: #1c9f8f;
    --fabric-pink: #e24c8a;
  }
  html, body {
    margin: 0;
    padding: 0;
    width: 1200px;
    height: 692px;
    overflow: hidden;
    background: var(--backdrop);
  }
  .business-card {
    position: absolute;
    left: 100px;
    top: 60px;
    width: 1000px;
    height: 572px;
    background: var(--card-black);
    overflow: hidden;
    box-shadow: 0 6px 18px rgba(0,0,0,0.25);
  }
  .brand-name {
    position: absolute;
    left: 140px;
    top: 150px;
    width: 470px;
    margin: 0;
    font-family: "Jost", sans-serif;
    font-weight: 700;
    font-size: 60px;
    line-height: 0.95;
    letter-spacing: 1px;
    text-transform: uppercase;
    color: var(--brand-red);
  }
  .brand-line {
    display: block;
    white-space: nowrap;
  }
  .brand-line--first {
    position: relative;
  }
  .brand-amp {
    position: absolute;
    left: 330px;
    top: -52px;
    font-size: 80px;
  }
  .brand-line--second {
    text-align: right;
  }
  .owner {
    position: absolute;
    left: 660px;
    top: 100px;
    width: 260px;
  }
  .owner-name {
    margin: 0 0 10px;
    font-family: "Jost", sans-serif;
    font-weight: 700;
    font-size: 21px;
    letter-spacing: 0.5px;
    text-transform: uppercase;
    color: var(--text-white);
    white-space: nowrap;
  }
  .owner-tag {
    display: block;
    width: 170px;
    height: 52px;
    background: var(--accent-yellow);
  }
  .contact {
    position: absolute;
    right: 430px;
    top: 300px;
    margin: 0;
    font-family: "Arimo", sans-serif;
    font-size: 22px;
    line-height: 1.45;
    color: var(--text-white);
    text-align: right;
    font-style: normal;
    white-space: nowrap;
  }
  .fabric-strip {
    position: absolute;
    left: 0;
    bottom: 0;
    width: 100%;
    height: 140px;
    background: linear-gradient(90deg,
      var(--fabric-red) 0%,
      var(--fabric-teal) 14%,
      var(--fabric-yellow) 26%,
      var(--fabric-pink) 38%,
      var(--fabric-blue) 52%,
      var(--fabric-red) 64%,
      var(--fabric-blue) 78%,
      var(--fabric-yellow) 100%);
  }
</style>
</head>
<body>
  <section class="business-card">
    <h1 class="brand-name">
      <span class="brand-line brand-line--first">Heritage<span class="brand-amp">&amp;</span></span>
      <span class="brand-line brand-line--second">Style</span>
    </h1>

    <div class="owner">
      <p class="owner-name">Folasade Okonkwo</p>
      <span class="owner-tag" role="img" aria-label="Yellow tag with African geometric pattern"></span>
    </div>

    <address class="contact">
      27846 Birchmont Court, Fernhill, NV 20894<br>
      Telephone: 318-731-5096<br>
      E-mail: heritageandstyle@mailvora.net
    </address>

    <div class="fabric-strip" role="img" aria-label="Photograph of colourful African print fabrics"></div>
  </section>
</body>
</html>
```